Car Detailing product label for 750ML Clear Bottle

I need a label for various product with differente color for each products but in the same size bottle each time. It's only for our purpose no commercial application. I need a template with differente color but same design. The name for product it's : Tidal Quartz. We dont have any logo because it's only for us. We like like car silhouette in the logo or in background or something like that.

And for the product we have many like : APC Cleaner, Drying Aid, Wheel Cleaner and some other.

```html
<!DOCTYPE html>
<html lang="en">
<head>
<meta charset="utf-8">
<title>APC All Purpose Cleaner – Label Template</title>
<link rel="stylesheet" href="https://fonts.googleapis.com/css2?family=Saira+Condensed:wght@600;800&family=Barlow+Semi+Condensed:wght@500;600&display=swap">
<style>
  :root {
    --page: #e8e9eb;
    --label-black: #141414;
    --lime: #d5e22b;
    --steel: #5a5a5a;
    --white: #ffffff;
  }
  * { box-sizing: border-box; margin: 0; padding: 0; }
  html, body { width: 1200px; height: 2568px; overflow: hidden; }
  body {
    background: var(--page);
    position: relative;
  }
  .label {
    position: absolute;
    top: 846px;
    width: 500px;
    height: 875px;
    background: var(--label-black);
    box-shadow: 8px 10px 18px rgba(0,0,0,0.35);
    overflow: hidden;
  }
  .label--front { left: 80px; }
  .label--back { left: 620px; }
  .label__shapes { position: absolute; inset: 0; width: 100%; height: 100%; }
  .label__car {
    position: absolute;
    border-radius: 50% 50% 12px 12px / 70% 70% 12px 12px;
    background: linear-gradient(180deg, rgba(213,226,43,0.55), rgba(213,226,43,0.08));
  }
  .label--front .label__car { left: 48px; top: 180px; width: 400px; height: 66px; }
  .label--back .label__car { left: 96px; top: 178px; width: 268px; height: 46px; }
  .headline {
    position: absolute;
    left: 0; right: 0;
    text-align: center;
    font-family: "Saira Condensed", sans-serif;
    font-weight: 800;
    color: var(--white);
    line-height: 1;
  }
  .headline--code { top: 268px; font-size: 128px; letter-spacing: 2px; }
  .headline--name { top: 380px; font-size: 90px; line-height: 79px; }
  .divider {
    position: absolute;
    left: 74px; width: 350px; top: 568px;
    height: 4px; background: var(--white);
  }
  .tagline {
    position: absolute;
    left: 0; right: 0; top: 580px;
    text-align: center;
    font-family: "Saira Condensed", sans-serif;
    font-weight: 600;
    font-size: 42px;
    line-height: 47px;
    color: var(--lime);
  }
  .volume {
    position: absolute;
    left: 0; right: 0; top: 772px;
    text-align: center;
    font-family: "Barlow Semi Condensed", sans-serif;
    font-weight: 600;
    font-size: 34px;
    color: var(--white);
  }
  .description {
    position: absolute;
    left: 56px; right: 56px; top: 244px;
    text-align: center;
    font-family: "Barlow Semi Condensed", sans-serif;
    font-weight: 500;
    font-size: 22px;
    line-height: 31px;
    color: var(--white);
  }
  .use-icons {
    position: absolute;
    left: 0; right: 0; top: 541px;
    display: flex;
    justify-content: center;
    gap: 13px;
  }
  .use-icon {
    width: 102px; height: 102px;
    border: 2.5px solid var(--lime);
    border-radius: 50%;
    background: radial-gradient(circle, rgba(213,226,43,0.28) 0 38%, transparent 40%);
  }
</style>
</head>
<body>

<section class="label label--front">
  <svg class="label__shapes" viewBox="0 0 393 687" preserveAspectRatio="none" aria-hidden="true">
    <polygon points="0,95 40,95 150,0 196,0 196,24 0,220" fill="var(--lime)"/>
    <polygon points="393,95 353,95 243,0 196,0 196,24 393,220" fill="var(--lime)"/>
    <polygon points="0,520 22,520 150,648 150,687 0,687" fill="var(--lime)"/>
    <polygon points="393,520 371,520 243,648 243,687 393,687" fill="var(--lime)"/>
    <polygon points="22,556 60,556 94,590 56,590" fill="var(--steel)"/>
    <polygon points="371,556 333,556 299,590 337,590" fill="var(--steel)"/>
  </svg>
  <div class="label__car" role="img" aria-label="Line drawing of a sports car silhouette"></div>
  <h1 class="headline headline--code">APC</h1>
  <h2 class="headline headline--name">ALL PURPOSE<br>CLEANER</h2>
  <div class="divider"></div>
  <p class="tagline">MORE THAN<br>DETALING</p>
  <p class="volume">750ml</p>
</section>

<section class="label label--back">
  <svg class="label__shapes" viewBox="0 0 393 687" preserveAspectRatio="none" aria-hidden="true">
    <polygon points="0,95 40,95 150,0 196,0 196,24 0,220" fill="var(--lime)"/>
    <polygon points="393,95 353,95 243,0 196,0 196,24 393,220" fill="var(--lime)"/>
    <polygon points="0,520 22,520 150,648 150,687 0,687" fill="var(--lime)"/>
    <polygon points="393,520 371,520 243,648 243,687 393,687" fill="var(--lime)"/>
    <polygon points="22,556 60,556 94,590 56,590" fill="var(--steel)"/>
    <polygon points="371,556 333,556 299,590 337,590" fill="var(--steel)"/>
  </svg>
  <div class="label__car" role="img" aria-label="Line drawing of a sports car silhouette"></div>
  <p class="description">Lorem ipsum dolor sit amet, consectetuer adipiscing elit, sed diam nonummy nibh euismod tincidunt ut laoreet dolore magna aliquam erat volutpat. Ut wisi enim ad minim veniam, quis nostrud exerci tation ullamcorper suscipit lobortis, Ut wisi enim ad minim veniam, quis nostrud exerci tation ullamcorper suscipit lobortis</p>
  <div class="use-icons">
    <div class="use-icon" role="img" aria-label="Jacket icon"></div>
    <div class="use-icon" role="img" aria-label="Shoe icon"></div>
    <div class="use-icon" role="img" aria-label="Sofa icon"></div>
  </div>
  <p class="volume">750ml</p>
</section>

</body>
</html>
```